Blue Ridge Harbor Home Inc. Website Update

We have a couple of broken links such as the "contact us" and would like to add board members and a calendar of events. We are open to a new design.

```html
<!DOCTYPE html>
<html lang="en">
<head>
<meta charset="utf-8">
<title>Blue Ridge Harbor Home Inc. — Events, Board Members, Contact</title>
<link rel="stylesheet" href="https://fonts.googleapis.com/css2?family=Poppins:wght@600&family=Raleway:wght@400;500;600;700&family=Roboto:wght@400;500&display=swap">
<style>
:root{
  --brand-blue:#0b77b8;
  --accent-cyan:#16b9e8;
  --ink:#111111;
  --line:#555555;
  --calendar-head:#8fb1ec;
  --panel-bg:#e6f4fd;
  --panel-border:#7e8ea8;
  --photo-back:#b9bdc8;
  --photo-mid:#4e5a7a;
  --white:#ffffff;
}
*{box-sizing:border-box;margin:0;padding:0}
html,body{width:671px;height:1200px;overflow:hidden;background:var(--white)}
.canvas{position:relative;width:671px;height:1200px;overflow:hidden}
.stage{position:absolute;left:0;top:0;width:830px;height:1500px;transform:scale(.8084,.8);transform-origin:0 0;font-family:"Raleway",sans-serif;color:var(--ink)}
.abs{position:absolute}
.section-title{position:absolute;left:0;width:830px;text-align:center;font-family:"Poppins",sans-serif;font-weight:600;font-size:31px;color:var(--brand-blue);letter-spacing:.2px}

/* calendar */
.calendar{left:164px;top:128px;width:169px;border-collapse:collapse;font-family:"Raleway",sans-serif;font-size:8px;font-weight:700}
.calendar caption{background:var(--calendar-head);border:1px solid var(--line);border-bottom:0;height:13px;line-height:12px;font-size:8px;word-spacing:2px}
.calendar td,.calendar th{border:1px solid var(--line);height:14px;text-align:center;padding:0;font-weight:700}
.calendar .week{width:20px;font-weight:600}
.calendar .today{background:var(--brand-blue);color:var(--white)}

/* search panel */
.search-panel{left:164px;top:240px;width:169px;height:207px;background:var(--panel-bg);border:1px solid var(--panel-border);font-size:8px}
.search-panel__head{background:var(--calendar-head);height:14px;line-height:13px;padding-left:6px;font-weight:700;border-bottom:1px solid var(--panel-border)}
.search-panel .label{position:absolute;left:6px;font-weight:700}
.search-panel .field{position:absolute;left:6px;height:10px;border-radius:5px;background:var(--white);font-size:6px;line-height:10px;padding-left:5px;color:#555}
.search-panel .field.select::after{content:"⌄";position:absolute;right:4px;top:-2px;font-size:8px;color:#000}
.search-panel .row{position:absolute;left:6px;font-size:8px}
.search-panel .date{position:absolute;left:54px;height:10px;line-height:10px;padding:0 4px;border-radius:5px;background:var(--white);font-weight:700;font-size:7.5px}
.search-panel .button{position:absolute;left:6px;top:176px;height:14px;line-height:14px;padding:0 8px;border-radius:7px;background:var(--white);font-size:8px}

/* events list */
.events{left:349px;top:129px;width:326px;height:520px;border:1px solid var(--line)}
.events__date{position:absolute;left:15px;top:6px;font-weight:700;font-size:15px;letter-spacing:.6px}
.event{position:absolute;left:15px;width:305px}
.event__time{color:var(--brand-blue);font-weight:500;font-size:14.5px;line-height:18px}
.event__text{font-size:16px;line-height:19px}

/* board */
.member{position:absolute;top:772px;width:160px}
.member__photo{position:relative;width:141px;height:183px}
.member__photo .back{position:absolute;left:12px;top:0;width:129px;height:175px;border-radius:30px;background:var(--photo-back)}
.member__photo .mid{position:absolute;left:6px;top:4px;width:129px;height:177px;border-radius:30px;background:var(--photo-mid)}
.member__photo .portrait{position:absolute;left:0;top:7px;width:131px;height:176px;border-radius:30px;background:linear-gradient(180deg,#7d7e80 0%,#77787a 60%,#3a4266 100%)}
.member__name{position:absolute;top:205px;font-family:"Roboto",sans-serif;font-weight:500;font-size:12.5px;white-space:nowrap}
.member__bio{position:absolute;top:235px;width:170px;font-family:"Roboto",sans-serif;font-size:10px;line-height:12.6px;white-space:nowrap}
.member__more{position:absolute;top:323px;font-family:"Roboto",sans-serif;font-size:10px;color:var(--brand-blue);text-decoration:none;white-space:nowrap}
.member__more span{color:var(--ink)}

/* contact */
.contact-text{left:164px;top:1217px;width:270px;font-family:"Raleway",sans-serif;font-size:13.3px;line-height:15.8px;font-weight:500;white-space:nowrap}
.input{position:absolute;left:441px;width:234px;height:22px;border:1.5px solid var(--accent-cyan);border-radius:4px;background:var(--white);font-family:"Roboto",sans-serif;font-size:13px}
.input__icon{position:absolute;left:-1.5px;top:-1.5px;width:42px;height:22px;background:var(--brand-blue);display:flex;align-items:center;justify-content:center}
.input__label{position:absolute;left:48px;top:2px}
.message{position:absolute;left:441px;top:1300px;width:234px;height:92px;border:1.5px solid var(--accent-cyan);border-radius:4px;padding:4px 9px;font-family:"Roboto",sans-serif;font-size:13px;color:#333}
.submit{position:absolute;left:441px;top:1413px;width:110px;height:21px;border-radius:3px;background:var(--accent-cyan);color:var(--white);font-family:"Roboto",sans-serif;font-weight:500;font-size:12.5px;line-height:21px;text-align:center;letter-spacing:.4px}
</style>
</head>
<body>
<div class="canvas">
<main class="stage">

  <h2 class="section-title" style="top:56px">Our Events</h2>

  <table class="calendar abs">
    <caption>&lt;&lt; &nbsp; March 2019 &nbsp; &gt;&gt;</caption>
    <tr><th class="week">w</th><th>Su</th><th>Mo</th><th>Tu</th><th>We</th><th>Th</th><th>Fr</th><th>Sa</th></tr>
    <tr><td class="week">w</td><td></td><td>1</td><td>2</td><td>3</td><td>4</td><td>5</td><td>6</td></tr>
    <tr><td class="week">w</td><td>7</td><td>8</td><td class="today">9</td><td>10</td><td>11</td><td>12</td><td>13</td></tr>
    <tr><td class="week">w</td><td>14</td><td>15</td><td>16</td><td>17</td><td>18</td><td>19</td><td>20</td></tr>
    <tr><td class="week">w</td><td>21</td><td>22</td><td>23</td><td>24</td><td>25</td><td>26</td><td>27</td></tr>
    <tr><td class="week">w</td><td>28</td><td>29</td><td>30</td><td>31</td><td></td><td></td><td></td></tr>
  </table>

  <form class="search-panel abs">
    <div class="search-panel__head">Search By :</div>
    <div class="label" style="top:24px">Fields :</div>
    <div class="field" style="top:38px;width:70px">Keyword</div>
    <div class="field select" style="top:53px;width:85px">Category</div>
    <div class="field select" style="top:66px;width:85px">Sub Category</div>
    <div class="label" style="top:95px">Date Range :</div>
    <div class="row" style="top:113px">Start Date :</div>
    <div class="date" style="top:113px">03/03/19 ⌄</div>
    <div class="row" style="top:127px">End Date :</div>
    <div class="date" style="top:127px">31/03/19 ⌄</div>
    <div class="row" style="top:153px">
      <svg width="8" height="8" viewBox="0 0 8 8" style="vertical-align:-1px"><path d="M1 4.2 3 6.3 7 1.5" fill="none" stroke="#000" stroke-width="1.3"/></svg>
      &nbsp;Include date range</div>
    <div class="button">Search</div>
  </form>

  <section class="events abs">
    <div class="events__date">09/03/19</div>
    <div class="event" style="top:63px"><div class="event__time">07:15 - 10:15</div><p class="event__text">Lorem Ipsum is simply dummy text of the printing and typesetting industry.</p></div>
    <div class="event" style="top:157px"><div class="event__time">07:15 - 10:15</div><p class="event__text">Lorem Ipsum is simply dummy text of the printing and typesetting industry.</p></div>
    <div class="event" style="top:252px"><div class="event__time">07:15 - 10:15</div><p class="event__text">Lorem Ipsum is simply dummy text of the printing and typesetting industry.</p></div>
    <div class="event" style="top:346px"><div class="event__time">07:15 - 10:15</div><p class="event__text">Lorem Ipsum is simply dummy text of the printing and typesetting industry.</p></div>
    <div class="event" style="top:441px"><div class="event__time">07:15 - 10:15</div><p class="event__text">Lorem Ipsum is simply dummy text of the printing and typesetting industry.</p></div>
  </section>

  <h2 class="section-title" style="top:707px;left:-12px">Our Board Members</h2>

  <article class="member" style="left:164px">
    <div class="member__photo"><div class="back"></div><div class="mid"></div><div class="portrait" role="img" aria-label="Portrait photo of a board member"></div></div>
    <h3 class="member__name">Lorem Ipsum</h3>
    <p class="member__bio">Contrary to popular belief,<br>Lorem Ipsum is not simply<br>random text. It has roots in a<br>piece of classical Latin literature<br>from 45 BC, making it over 2000<br>years old.</p>
    <a class="member__more" href="#">Read More <span>&gt;&gt;</span></a>
  </article>
  <article class="member" style="left:349px">
    <div class="member__photo"><div class="back"></div><div class="mid"></div><div class="portrait" role="img" aria-label="Portrait photo of a board member"></div></div>
    <h3 class="member__name" style="left:-2px">Lorem Ipsum</h3>
    <p class="member__bio" style="left:-2px">Contrary to popular belief,<br>Lorem Ipsum is not simply<br>random text. It has roots in a<br>piece of classical Latin literature<br>from 45 BC, making it over 2000<br>years old.</p>
    <a class="member__more" href="#" style="left:-2px">Read More <span>&gt;&gt;</span></a>
  </article>
  <article class="member" style="left:534px">
    <div class="member__photo"><div class="back"></div><div class="mid"></div><div class="portrait" role="img" aria-label="Portrait photo of a board member"></div></div>
    <h3 class="member__name" style="left:-8px">Lorem Ipsum</h3>
    <p class="member__bio" style="left:-8px">Contrary to popular belief,<br>Lorem Ipsum is not simply<br>random text. It has roots in a<br>piece of classical Latin literature<br>from 45 BC, making it over 2000<br>years old.</p>
    <a class="member__more" href="#" style="left:-8px">Read More <span>&gt;&gt;</span></a>
  </article>

  <h2 class="section-title" style="top:1161px;left:8px">Contact Us</h2>

  <p class="contact-text abs">Lorem Ipsum is simply dummy text of the<br>printing and typesetting industry. Lorem<br>Ipsum has been the industry's standard<br>dummy text ever since the 1500s, when<br>an unknown printer took a galley of type<br>and scrambled it to make a type speci-<br>men book. It has survived not only five<br>centuries, but also the leap into electronic<br>typesetting, remaining essentially un-<br>changed.</p>

  <div class="input" style="top:1220px">
    <span class="input__icon"><svg width="10" height="11" viewBox="0 0 10 11"><circle cx="5" cy="3" r="2.4" fill="#fff"/><path d="M1 11v-2.5C1 6.8 2.6 6 5 6s4 .8 4 2.5V11z" fill="#fff"/></svg></span>
    <span class="input__label">Name</span>
  </div>
  <div class="input" style="top:1262px">
    <span class="input__icon"><svg width="12" height="8" viewBox="0 0 12 8"><rect x=".5" y=".5" width="11" height="7" fill="#fff"/><path d="M.5 .5 6 4.5 11.5 .5" fill="none" stroke="#0b77b8" stroke-width="1"/></svg></span>
    <span class="input__label">Email</span>
  </div>
  <div class="message">Your Text Here</div>
  <div class="submit">SUBMIT</div>

</main>
</div>
</body>
</html>
```